Visitenkarte erstellen für Reiki Praxis

Visitenkarten für Reiki Praxis Doppelseitig

business cards reiki practice double-sided

The background can also be a different color

```html
<!DOCTYPE html>
<html lang="en">
<head>
<meta charset="UTF-8">
<title>Stillwater Reiki – Business Cards</title>
<link rel="stylesheet" href="https://fonts.googleapis.com/css2?family=Montserrat:wght@300;400;500;800&display=swap">
<style>
  :root {
    --bg: #2b2b2b;
    --card-black: #181818;
    --white: #ffffff;
    --gold: #e0a622;
    --peach: #f7a873;
    --sage: #97a08f;
    --rose: #c27ca0;
    --soft-peach: #f0b48a;
  }
  html, body {
    margin: 0;
    width: 1200px;
    height: 900px;
    overflow: hidden;
    background: var(--bg);
    font-family: "Montserrat", Arial, sans-serif;
  }
  .stage {
    width: 1200px;
    height: 900px;
    display: flex;
    flex-direction: column;
    align-items: center;
    justify-content: center;
    gap: 34px;
  }
  .card {
    position: relative;
    width: 700px;
    height: 400px;
    border-radius: 26px;
    overflow: hidden;
    background: var(--card-black);
    box-shadow: 0 14px 30px rgba(0,0,0,.45);
  }
  /* front */
  .card-front {
    background: linear-gradient(125deg, var(--peach) 8%, var(--sage) 50%, var(--rose) 85%);
  }
  .front-shape {
    position: absolute;
    inset: 0;
  }
  .contact-block {
    position: absolute;
    left: 46px;
    top: 60px;
    color: var(--white);
  }
  .person-name {
    margin: 0;
    font-weight: 800;
    font-size: 36px;
    letter-spacing: 1px;
    text-transform: uppercase;
  }
  .person-role {
    margin: 2px 0 26px;
    font-weight: 400;
    font-size: 17px;
    letter-spacing: 1px;
    text-transform: uppercase;
  }
  .contact-list {
    list-style: none;
    margin: 0;
    padding: 0;
    font-size: 16px;
    line-height: 1.6;
  }
  .contact-list li {
    display: flex;
    align-items: center;
    gap: 9px;
  }
  .contact-list svg { width: 14px; height: 14px; flex: none; }
  .brand-block {
    position: absolute;
    left: 350px;
    top: 208px;
    width: 330px;
    text-align: center;
  }
  .brand-name {
    margin: 0;
    color: var(--white);
    font-weight: 300;
    font-size: 27px;
    letter-spacing: 3px;
    text-transform: uppercase;
  }
  .brand-owner {
    margin: 4px 0 0;
    color: var(--gold);
    font-weight: 400;
    font-size: 17px;
    letter-spacing: 7px;
    text-transform: uppercase;
  }
  /* back */
  .card-back {
    display: flex;
    align-items: center;
    justify-content: center;
    gap: 18px;
  }
  .back-dot {
    width: 26px;
    height: 26px;
    border-radius: 50%;
    border: 2px solid var(--soft-peach);
  }
  .back-name {
    margin: 0;
    color: var(--soft-peach);
    font-weight: 300;
    font-size: 40px;
    letter-spacing: 5px;
    text-transform: uppercase;
  }
</style>
</head>
<body>
<main class="stage">
  <section class="card card-front" aria-label="Business card front">
    <svg class="front-shape" viewBox="0 0 700 400" aria-hidden="true">
      <circle cx="598" cy="352" r="330" fill="var(--gold)"/>
      <circle cx="610" cy="352" r="320" fill="var(--card-black)"/>
    </svg>
    <div class="contact-block">
      <h1 class="person-name">Daniel Hart</h1>
      <p class="person-role">Director</p>
      <ul class="contact-list">
        <li>
          <svg viewBox="0 0 24 24" aria-hidden="true"><path fill="#fff" d="M6.6 10.8a15 15 0 0 0 6.6 6.6l2.2-2.2c.3-.3.7-.4 1-.2 1.1.4 2.3.6 3.6.6.6 0 1 .4 1 1V20c0 .6-.4 1-1 1A17 17 0 0 1 3 4c0-.6.4-1 1-1h3.5c.6 0 1 .4 1 1 0 1.3.2 2.5.6 3.6.1.3 0 .7-.2 1z"/></svg>
          330 555 0142
        </li>
        <li>
          <svg viewBox="0 0 24 24" aria-hidden="true"><rect x="3" y="5" width="18" height="14" rx="1.5" fill="none" stroke="#fff" stroke-width="2"/><path d="M3 6l9 7 9-7" fill="none" stroke="#fff" stroke-width="2"/></svg>
          info@stillwaterreiki.com
        </li>
        <li>
          <svg viewBox="0 0 24 24" aria-hidden="true"><circle cx="12" cy="12" r="9" fill="none" stroke="#fff" stroke-width="2"/><path d="M3 12h18M12 3c3 3 3 15 0 18M12 3c-3 3-3 15 0 18" fill="none" stroke="#fff" stroke-width="1.6"/></svg>
          www.stillwaterreiki.com
        </li>
      </ul>
    </div>
    <div class="brand-block">
      <p class="brand-name">Stillwater Reiki</p>
      <p class="brand-owner">Mara Linden</p>
    </div>
  </section>

  <section class="card card-back" aria-label="Business card back">
    <span class="back-dot" aria-hidden="true"></span>
    <p class="back-name">Stillwater Reiki</p>
  </section>
</main>
</body>
</html>
```